Brindlefax Brochure

I require a brochure for my business called Brindlefax Services or "Brindlefax" for short. We obtain subpoena material on behalf of lawfirms in Sydney and focus purely on the sydney-city based locations.

www.brindlefax-demo.com.au

My website is quite comprehensive and has all the information you may require.

The design should stand out as to price and trust to know we would complete the job professionally remember that my clients are law firms. I have a few documents that i will attach that will show you what i am looking for. I will leave colour upto the designer.

I require ongoing work including logos, other brochures so this will be an ongoing contract. I require someone who will communicate with me and is available for a range of projects.

Target Market(s)

Law firms

Industry/Entity Type

Business

Colors

Designer to choose colors to be used in the design.

Requirements
Must have
• professional and instill trust and security
Nice to have
• this market is dominated by 3 other firms we are a new firm looking to establish and take a number of their clients who are paying through the nose.

```html
<!DOCTYPE html>
<html lang="en">
<head>
<meta charset="utf-8">
<title>Brindlefax Services – Brochure</title>
<link href="https://fonts.googleapis.com/css2?family=Jost:wght@400;500;800&display=swap" rel="stylesheet">
<style>
  :root {
    --page-bg: #ffffff;
    --sky-pale: #e2f0fb;
    --sky-soft: #d3e8f8;
    --brand-blue: #22b8ec;
    --ink-teal: #0d4f5e;
    --ink-grey: #2b2b2b;
    --paper-white: #ffffff;
  }
  html, body {
    margin: 0;
    width: 1200px;
    height: 1000px;
    overflow: hidden;
    background: var(--page-bg);
    font-family: "Jost", "Futura", sans-serif;
  }
  .canvas {
    position: relative;
    width: 1200px;
    height: 1000px;
  }
  .brochure {
    position: absolute;
    left: 390px;
    top: 50px;
    width: 420px;
    height: 900px;
    display: flex;
    flex-direction: column;
    box-shadow: 0 0 0 1px rgba(0,0,0,0.04);
  }
  .brochure__cover {
    position: relative;
    height: 520px;
    background: linear-gradient(170deg, var(--sky-pale) 0%, var(--sky-soft) 100%);
  }
  .hex-pattern {
    position: absolute;
    inset: 0;
  }
  .brand {
    position: absolute;
    left: 0;
    right: 0;
    top: 150px;
    text-align: center;
    color: var(--ink-grey);
    font-weight: 400;
  }
  .brand__name {
    display: block;
    font-size: 50px;
    line-height: 1;
    letter-spacing: 0.5px;
  }
  .brand__tag {
    display: block;
    margin-top: 8px;
    font-size: 20px;
    letter-spacing: 1px;
  }
  .brochure__panel {
    flex: 1;
    background: var(--brand-blue);
    padding: 40px 36px 36px;
    display: flex;
    flex-direction: column;
  }
  .headline {
    margin: 0 0 26px;
    color: var(--ink-teal);
    font-weight: 800;
    font-size: 33px;
    line-height: 1.02;
    text-transform: uppercase;
    letter-spacing: 0.3px;
  }
  .services__intro {
    margin: 0;
    color: var(--paper-white);
    font-weight: 500;
    font-size: 17px;
    line-height: 1.3;
  }
  .services__list {
    margin: 0;
    padding: 0 0 0 14px;
    color: var(--paper-white);
    font-weight: 500;
    font-size: 17px;
    line-height: 1.3;
  }
  .website {
    margin-top: auto;
    color: var(--ink-teal);
    font-weight: 800;
    font-size: 24px;
    letter-spacing: 0.3px;
    text-transform: uppercase;
  }
</style>
</head>
<body>
<div class="canvas">
  <article class="brochure">
    <section class="brochure__cover">
      <div class="hex-pattern" role="img" aria-label="Faint honeycomb background pattern in pale blue"></div>
      <div class="brand">
        <span class="brand__name">Brindlefax</span>
        <span class="brand__tag">Services</span>
      </div>
    </section>
    <section class="brochure__panel">
      <h1 class="headline">Need important legal documents delivered urgently?</h1>
      <p class="services__intro">Onsite coping and uplifting of documents and court records at:</p>
      <ul class="services__list">
        <li>Local Courts - Harlow centre Sydney and Edwin Carrow Town</li>
        <li>District Courts</li>
        <li>Family Court</li>
        <li>NSW Supreme Court</li>
      </ul>
      <div class="website">www.brindlefax-demo.com.au</div>
    </section>
  </article>
</div>
</body>
</html>
```